Pup Snack Den - New Website Design

Create a professional Vendora website for a the hottest trend; a Pup Snack Den subscription box business. Vendora.com is an easy to use website builder.
Please see frillnest.example; sugarloop.example and woofcrate.example for the concept I am after. The business has not been launched yet, I am currently in the pre-launch stage using a specialized landing page website, and so the time scale for developing my professional looking Vendora website is up to 1-2 weeks.
The webpage should have a fun feel and should match the style of the company logo at sugarloop.example. The pages to include are 'Home', 'About us' and 'Get Started'
Thank you and good luck!
Industry/Entity Type
Business
Coding
Coded - Design and coding required
Number of Pages Required
1 page
Look and feel
Each slider illustrates characteristics of the customer's brand and the style your logo design should communicate.

```html
<!DOCTYPE html>
<html lang="en">
<head>
<meta charset="utf-8">
<title>Pup Snack Den</title>
<link rel="stylesheet" href="https://fonts.googleapis.com/css2?family=Philosopher:wght@400;700&family=Open+Sans:wght@400;600&family=Kanit:wght@400;500&family=Oswald:wght@500;600&family=Roboto+Slab:wght@400&display=swap">
<style>
:root{
  --green:#8cc63f;
  --lime:#a7c520;
  --yellow:#f0e442;
  --brown:#5a3510;
  --ink:#2b2b2b;
  --grey:#777;
  --light:#bdbdbd;
  --dark:#333333;
  --white:#ffffff;
}
*{margin:0;padding:0;box-sizing:border-box}
html,body{width:1200px;height:2995px;overflow:hidden;background:var(--white)}
body{position:relative;font-family:"Open Sans",sans-serif;color:var(--ink)}
.abs{position:absolute}
/* header */
.site-header{left:0;top:0;width:1200px;height:104px;background:var(--white)}
.brand{left:80px;top:28px;font:700 40px "Philosopher",serif;color:var(--green);display:flex;align-items:center;gap:12px}
.brand-dot{width:22px;height:22px;border-radius:50%;background:var(--brown)}
.main-nav{left:460px;top:50px;display:flex;gap:30px;font:400 15px "Open Sans",sans-serif;color:var(--ink)}
.header-social{left:774px;top:44px;display:flex;gap:10px}
.header-social span{width:28px;height:28px;border-radius:50%;background:#c9c9c9}
.login{left:942px;top:52px;font:600 13px "Open Sans",sans-serif;color:var(--ink)}
.signup{left:1012px;top:51px;width:104px;height:24px;background:var(--green);color:var(--white);font:600 12px "Open Sans",sans-serif;display:flex;align-items:center;justify-content:center}
/* hero */
.hero{left:0;top:104px;width:1200px;height:544px;background:linear-gradient(100deg,#4a5e22 0%,#7a9a3a 40%,#9bb860 70%,#5d7430 100%)}
.hero-title{left:86px;top:268px;font:400 52px "Philosopher",serif;color:var(--white)}
.hero-text{left:90px;top:336px;width:470px;font:400 14px/22px "Open Sans",sans-serif;color:var(--white)}
.hero-btn{left:86px;top:434px;width:204px;height:50px;background:var(--green);border-radius:3px;color:var(--white);font:600 20px "Open Sans",sans-serif;display:flex;align-items:center;justify-content:center}
/* intro */
.intro-title{left:0;top:712px;width:1200px;text-align:center;font:700 54px "Philosopher",serif;color:var(--brown)}
.intro-text{left:140px;width:920px;text-align:center;font:400 14px/26px "Open Sans",sans-serif;color:var(--grey)}
/* services */
.service{width:212px;text-align:center}
.service-photo{width:212px;height:212px;border-radius:50%;border:5px solid var(--yellow)}
.service-go{position:absolute;left:74px;top:172px;width:64px;height:64px;border-radius:50%;background:var(--lime);display:flex;align-items:center;justify-content:center}
.service-name{margin-top:50px;font:400 24px "Kanit",sans-serif;color:var(--ink)}
/* testimonials */
.testimonials{left:0;top:1488px;width:1200px;height:392px;background:linear-gradient(90deg,#1c1c1c,#3b3a33 50%,#1e1e1e)}
.quote-avatar{width:86px;height:86px;border-radius:50%;background:#8a6a48;border:3px solid var(--white)}
.quote-badge{width:18px;height:18px;border-radius:50%;background:var(--green);border:2px solid var(--white)}
.quote-name{font:600 17px "Oswald",sans-serif;color:var(--white);letter-spacing:.3px}
.quote-name em{font-style:normal;color:var(--lime)}
.quote-rule{width:36px;height:2px;background:var(--lime)}
.quote-text{width:370px;font:400 13.5px/20px "Roboto Slab",serif;color:var(--white)}
.dot{width:8px;height:8px;border-radius:50%;background:#666}
.dot.on{background:var(--lime)}
/* blog */
.blog-title{left:0;top:1986px;width:1200px;text-align:center;font:700 54px "Philosopher",serif;color:var(--ink)}
.blog-sub{left:0;top:2088px;width:1200px;text-align:center;font:400 14px "Roboto Slab",serif;color:var(--grey)}
.blog-rule{left:444px;top:2130px;width:304px;height:1px;background:#ddd}
.blog-rule-accent{left:572px;top:2129px;width:54px;height:3px;background:var(--lime)}
.post{width:302px}
.post-photo{width:302px;height:210px;border-radius:6px}
.post-date{position:absolute;left:18px;top:182px;width:56px;height:56px;border-radius:50%;background:var(--lime);color:var(--white);font:600 11px/13px "Oswald",sans-serif;display:flex;flex-direction:column;align-items:center;justify-content:center}
.post-title{margin-top:44px;font:600 18px/22px "Oswald",sans-serif;color:var(--ink);text-transform:uppercase}
.post-text{margin-top:10px;font:400 14px/19px "Roboto Slab",serif;color:var(--grey)}
.post-more{margin-top:22px;width:138px;height:34px;border:1px solid #ccc;border-radius:17px;display:flex;align-items:center;justify-content:center;font:500 12px "Oswald",sans-serif;color:var(--ink)}
/* subscribe */
.subscribe{left:0;top:2700px;width:1200px;height:118px;background:var(--lime)}
.sub-title{left:106px;top:2736px;font:600 21px "Oswald",sans-serif;color:var(--white)}
.sub-text{left:106px;top:2764px;font:400 13px "Open Sans",sans-serif;color:var(--white)}
.sub-field{left:406px;top:2740px;width:344px;height:36px;border:2px solid var(--white);border-radius:18px;color:var(--white);font:400 15px "Open Sans",sans-serif;padding-left:18px;display:flex;align-items:center}
.sub-social{left:856px;top:2740px;display:flex;gap:10px}
.sub-social span{width:38px;height:38px;border-radius:50%;border:2px solid var(--white)}
/* footer */
.site-footer{left:0;top:2818px;width:1200px;height:177px;background:var(--dark)}
.foot-brand{left:92px;top:2892px;font:700 40px "Philosopher",serif;color:var(--lime);display:flex;align-items:center;gap:12px}
.foot-brand .brand-dot{background:var(--white)}
.contact{left:440px;width:400px;text-align:center;font:400 14px "Open Sans",sans-serif;color:var(--white);display:flex;justify-content:center;align-items:center;gap:8px}
.follow{left:852px;top:2852px;width:160px;text-align:center;font:600 18px "Oswald",sans-serif;color:var(--white)}
.foot-social{left:830px;top:2898px;display:flex;gap:12px}
.foot-social span{width:44px;height:44px;border-radius:50%;background:var(--lime)}
.copyright{left:0;top:2958px;width:1200px;text-align:center;font:400 12px "Open Sans",sans-serif;color:#ccc}
</style>
</head>
<body>

<header class="abs site-header">
</header>
<div class="abs brand"><span class="brand-dot"></span>Pup Snack Den</div>
<nav class="abs main-nav"><span>HOME</span><span>ABOUT US</span><span>GET STARTED</span></nav>
<div class="abs header-social"><span></span><span></span><span></span><span></span></div>
<div class="abs login">Log In</div>
<div class="abs signup">SIGN UP</div>

<section class="abs hero" role="img" aria-label="Photo of a smiling man kneeling in a sunny park with a husky dog"></section>
<h1 class="abs hero-title">For the Love &amp; Care</h1>
<p class="abs hero-text">Donec a nisl a dolor dignissim porttitor. Integer ultricies sagittis viverra, Integer feugiat at dolor sed elementum. Vestibulum tincidunt dictum enim vitae fermentum</p>
<div class="abs hero-btn">Get Started</div>

<h2 class="abs intro-title">For the Love &amp; Care</h2>
<p class="abs intro-text" style="top:814px">Beciegast nveriti vitaesaert asety kertya aserde nerafae kertyuraue styasnemo faseriasera khatrsasas ptaiadeser asrolern atur aut oditaut. Densequntur magni dolquitione voluptatemsequi nesciunt orase joasuaserya vytarsa.</p>
<p class="abs intro-text" style="top:892px">Numquam eius modi teincidunt, ut labore et dolore magnam vitaesaert asety kertya aserde nerafae kertyuraue styasnemo faseriasera khatrsasas ptaiadeser asrolern atur aut oditaut. Densequntur magni dolquitione voluptatemsequi nesciunt orase joasuaserya vytarsa numquam eius modi teincidunt, ut labore et dolore magnam liaseras.</p>

<div class="abs service" style="left:96px;top:1064px">
  <div class="service-photo" role="img" aria-label="Dog sleeping and dreaming of treats" style="background:linear-gradient(#fafafa,#d9b68a)"></div>
  <div class="service-go"><svg width="22" height="22" viewBox="0 0 22 22"><path d="M8 4l7 7-7 7" fill="none" stroke="#fff" stroke-width="3"/></svg></div>
  <div class="service-name">Dog Dreams</div>
</div>
<div class="abs service" style="left:356px;top:1064px">
  <div class="service-photo" role="img" aria-label="Girl training a puppy" style="background:linear-gradient(#fafafa,#d8c6a8)"></div>
  <div class="service-go"><svg width="22" height="22" viewBox="0 0 22 22"><path d="M8 4l7 7-7 7" fill="none" stroke="#fff" stroke-width="3"/></svg></div>
  <div class="service-name">About their dogs</div>
</div>
<div class="abs service" style="left:628px;top:1064px">
  <div class="service-photo" role="img" aria-label="Kitten sitting on a dog" style="background:linear-gradient(#f4f4f4,#cbb49a)"></div>
  <div class="service-go"><svg width="22" height="22" viewBox="0 0 22 22"><path d="M8 4l7 7-7 7" fill="none" stroke="#fff" stroke-width="3"/></svg></div>
  <div class="service-name">Brushing</div>
</div>
<div class="abs service" style="left:894px;top:1064px">
  <div class="service-photo" role="img" aria-label="Long-haired cat lying down" style="background:linear-gradient(#e4e4e4,#9a8a76)"></div>
  <div class="service-go"><svg width="22" height="22" viewBox="0 0 22 22"><path d="M8 4l7 7-7 7" fill="none" stroke="#fff" stroke-width="3"/></svg></div>
  <div class="service-name">Cat Grooming</div>
</div>

<section class="abs testimonials" role="img" aria-label="Dark photo of people walking dogs on a path"></section>
<div class="abs quote-avatar" role="img" aria-label="Customer portrait" style="left:104px;top:1638px"></div>
<div class="abs quote-badge" style="left:170px;top:1642px"></div>
<div class="abs quote-name" style="left:212px;top:1622px">PAWLINE STUDIO / <em>WEB DESIGNER</em></div>
<div class="abs quote-rule" style="left:212px;top:1662px"></div>
<p class="abs quote-text" style="left:212px;top:1676px">Definitely see a difference in his coat! It's very inexpensive! Thank you for coming out with a more natural recipe for our dogs!</p>

<div class="abs quote-avatar" role="img" aria-label="Customer portrait" style="left:606px;top:1638px"></div>
<div class="abs quote-badge" style="left:672px;top:1642px"></div>
<div class="abs quote-name" style="left:714px;top:1622px">PAWLINE STUDIO / <em>WEB DESIGNER</em></div>
<div class="abs quote-rule" style="left:714px;top:1662px"></div>
<p class="abs quote-text" style="left:714px;top:1676px">Definitely see a difference in his coat! It's very inexpensive! Thank you for coming out with a more natural recipe for our dogs!</p>

<div class="abs dot on" style="left:568px;top:1808px"></div>
<div class="abs dot" style="left:590px;top:1808px"></div>
<div class="abs dot" style="left:612px;top:1808px"></div>

<h2 class="abs blog-title">Latest Blog</h2>
<p class="abs blog-sub">Pet treats packed with nutritious ingredients, vitamins and supplements to help dogs.</p>
<div class="abs blog-rule"></div>
<div class="abs blog-rule-accent"></div>

<article class="abs post" style="left:112px;top:2168px">
  <div class="post-photo" role="img" aria-label="Person sitting on a bed with a small black dog" style="background:linear-gradient(#8a8fa8,#4b4a52)"></div>
  <div class="post-date"><span>JAN</span><span>16</span></div>
  <h3 class="post-title">Taste this! Kibblo freeze dried raw dog food</h3>
  <p class="post-text">Healthy and Fun Frozen Yogurt Snacks it's playtime meets snack time when you freeze everybody's favorite health food into colorful [...]</p>
  <div class="post-more">READ MORE</div>
</article>
<article class="abs post" style="left:448px;top:2168px">
  <div class="post-photo" role="img" aria-label="Dog eating from a pink bowl on grass" style="background:linear-gradient(#c9c9b9,#6e8a3a)"></div>
  <div class="post-date"><span>JAN</span><span>16</span></div>
  <h3 class="post-title">Lorem Ipsum is simply dummy text</h3>
  <p class="post-text">Healthy and Fun Frozen Yogurt Snacks it's playtime meets snack time when you freeze everybody's favorite health food into colorful [...]</p>
  <div class="post-more">READ MORE</div>
</article>
<article class="abs post" style="left:782px;top:2168px">
  <div class="post-photo" role="img" aria-label="Boy hugging a black and white dog outdoors" style="background:linear-gradient(#7aa04a,#3f6b2a)"></div>
  <div class="post-date"><span>JAN</span><span>16</span></div>
  <h3 class="post-title">Various versions have evolved over the years</h3>
  <p class="post-text">Healthy and Fun Frozen Yogurt Snacks it's playtime meets snack time when you freeze everybody's favorite health food into colorful [...]</p>
  <div class="post-more">READ MORE</div>
</article>

<section class="abs subscribe"></section>
<div class="abs sub-title">SUBSCRIBE TO US!</div>
<div class="abs sub-text">Subscribe to our monthly newsletter</div>
<div class="abs sub-field">Enter your email here</div>
<svg class="abs" style="left:712px;top:2750px" width="18" height="16" viewBox="0 0 18 16"><path d="M1 8l16-7-5 14-3-6z" fill="none" stroke="#fff" stroke-width="1.5"/></svg>
<div class="abs sub-social"><span></span><span></span><span></span><span></span><span></span></div>

<footer class="abs site-footer"></footer>
<div class="abs foot-brand"><span class="brand-dot"></span>Pup Snack Den</div>
<div class="abs contact" style="top:2856px">
  <svg width="14" height="14" viewBox="0 0 14 14"><path d="M3 1l3 3-2 2q2 3 4 4l2-2 3 3-2 2Q5 12 1 3z" fill="#8cc63f"/></svg>(000) 000-000</div>
<div class="abs contact" style="top:2882px">
  <svg width="16" height="12" viewBox="0 0 16 12"><rect width="16" height="12" fill="#8cc63f"/><path d="M0 0l8 6 8-6" fill="none" stroke="#333" stroke-width="1.2"/></svg>Email: hello@pupsnack.example</div>
<div class="abs contact" style="top:2908px">
  <svg width="10" height="14" viewBox="0 0 10 14"><path d="M5 14L1 7a4 4 0 1 1 8 0z" fill="#8cc63f"/><circle cx="5" cy="5" r="1.6" fill="#333"/></svg>45 Sample Lane, Riverton, RV2 8PQ</div>
<div class="abs follow">FOLLOW US</div>
<div class="abs foot-social"><span></span><span></span><span></span><span></span></div>
<div class="abs copyright">Copyright © 2017 - Designed by Pup Snack Den</div>

</body>
</html>
```